Food fans website needs a desktop homepage design

We need a desktop homepage design for TableHop.co.uk, a website to help you to find the best restaurants in each main city of Europe, with initial focus on London. It is not a directory with thousands of restaurants and reviews, else lists of top 20 restaurants for each area of the city. Food fans from all around the city will be able to keep an itinerary of where they eat, showing them later funny stats like "this month you really went for pizzas, don't you?". Keep it funny but professional.

A bit of branding has been done but this project give you total freedom to design the homepage of the site. The design must be a mix between minimal, flat and clean layout. The main idea is to keep it simple, easy to use and showing just the necessary elements.

For the font and colour scheme, we would like to use a thin but energetic font using the #E1393A colour as starting point even if you have freedom to slightly modify it. Blacks, greys and whites can be the secondary colours but we are open to introduce another main colour to the site like green, orange or yellow.

A simple wireframe has been attached to help you but the main elements that the page requires are the next:
- Panoramic fancy image in the header to contain the logo and the search form (the fields of the form are specified on the wireframe) and maybe some animated text to fill the right gap.
- List of results (10 results per page) showing the main info for each restaurant: name, thumbnail, location (zone, area), category, price, description, rating (no with stars please) and whatever you want to add that makes sense.
- Right hand sidebar with 3 widgets: Categories, Location and prices.

You can get the icons from glyphbarn.net.

We are open to have some text-shadows, rounded corners, box-shadows but trying to keep it minimal, flat and clean as much as possible. The main attractive of the site are the food/restaurant images.

Target Market(s)

22 - 45 food fans lovers from the city. busy people that want to disconnect and relax through the food. The don't mind to pay for quality and new experiences. Up to meet new places around them.

Industry/Entity Type

Restaurant

Requirements
Must have
• Panoramic image in the header, restaurants search form as per wireframe, list results with pagination, right hand sidebar with the widgets mention above and a nice footer with extra elements like "latest restaurants, latest tweets, etc.."
Nice to have
• This site will only be supported by the latest browsers so the idea is to have nice CSS3 transitions all around. Have that in mind at the time to design it even if you cannot show it on the design.
Should not have
• Busy backgrounds and unnecessary images that would slow down the page load.

```html
<!DOCTYPE html>
<html lang="en">
<head>
<meta charset="utf-8">
<title>TableHop London</title>
<link rel="stylesheet" href="https://fonts.googleapis.com/css2?family=Libre+Baskerville:wght@400;700&family=Jost:wght@300;400&family=Arimo:ital,wght@0,400;0,700;1,400&display=swap">
<style>
  :root {
    --red: #e1393a;
    --red-dark: #c92a2c;
    --ink: #2b2b2b;
    --text: #5a5a5a;
    --line: #d6d6d6;
    --field: #ffffff;
    --page: #ffffff;
    --footer: #444444;
    --footer-text: #8f8f8f;
    --footer-head: #c9c9c9;
    --page-btn: #b9b9b9;
    --icon: #666666;
  }
  * { box-sizing: border-box; margin: 0; padding: 0; }
  html, body { width: 1200px; height: 1032px; overflow: hidden; background: var(--page); }
  body { position: relative; font-family: "Arimo", Arial, sans-serif; color: var(--text); }
  .abs { position: absolute; }

  /* Header */
  .hero { left: 0; top: 0; width: 1200px; height: 449px;
    background: linear-gradient(180deg, #d9a57c 0%, #e2c59c 45%, #d8b48a 75%, #b06a4c 100%); }
  .site-title { left: 244px; top: 20px; font-family: "Libre Baskerville", Georgia, serif; font-weight: 700; font-size: 24px; color: #1d1d1d; }

  .search { left: 245px; top: 93px; width: 259px; height: 350px; background: #fff; }
  .search label { position: absolute; left: 18px; font-family: "Jost", Helvetica, sans-serif; font-weight: 300; font-size: 14.5px; color: #555; }
  .field { position: absolute; left: 18px; width: 227px; height: 33px; border: 1px solid #dcdcdc; background: var(--field);
    font-family: "Arimo", Arial, sans-serif; font-style: italic; font-size: 10px; color: #777; padding: 11px 0 0 9px; }
  .field svg { position: absolute; right: 9px; top: 11px; }
  .btn-search { position: absolute; left: 18px; top: 296px; width: 107px; height: 33px; background: linear-gradient(180deg, #ee4c4c, var(--red-dark));
    border-radius: 2px; color: #fff; font-family: "Jost", Helvetica, sans-serif; font-size: 14.5px; text-align: center; line-height: 33px;
    box-shadow: 0 6px 8px -4px rgba(0,0,0,.25); }

  .tagline { left: 550px; top: 133px; font-family: "Libre Baskerville", Georgia, serif; font-weight: 700; color: #4a4a4a; }
  .tagline h2 { font-size: 21px; font-weight: 700; }
  .tagline p.sub { font-size: 14px; margin-top: 4px; }
  .tagline p.small { font-size: 11px; margin-top: 30px; }

  /* Results */
  .results-title { left: 244px; top: 486px; font-family: "Libre Baskerville", Georgia, serif; font-weight: 700; font-size: 19px; color: var(--ink); letter-spacing: .3px; }
  .results-title span { color: var(--red); }
  .results-rule { left: 244px; top: 516px; width: 534px; height: 1px; background: var(--line); }

  .thumb { width: 165px; height: 122px; border: 1px solid var(--line); padding: 5px; background: #fff; }
  .thumb div { width: 100%; height: 100%; background: linear-gradient(135deg, #b9c28a 0%, #e3a552 45%, #d9664a 100%); }
  .item-name { font-family: "Libre Baskerville", Georgia, serif; font-weight: 700; font-size: 15px; color: var(--ink); }
  .item-desc { width: 335px; font-size: 9.6px; line-height: 13.4px; color: #666; }
  .item-more { font-size: 9px; font-weight: 700; color: #555; }
  .item-bar { left: 245px; width: 533px; height: 33px; border: 1px solid var(--line); display: flex; }
  .item-bar .cell { width: 41px; height: 31px; border-right: 1px solid var(--line); display: flex; align-items: center; justify-content: center; }
  .item-bar .rating { margin-left: auto; display: flex; gap: 4px; align-items: center; padding-right: 10px; }
  .rating i { width: 11px; height: 11px; border-radius: 50%; background: var(--red); display: block; }

  .pager { left: 246px; top: 899px; display: flex; gap: 3px; }
  .pager span { width: 26px; height: 23px; background: var(--page-btn); color: #333; font-size: 10px; text-align: center; line-height: 23px; }
  .pager span.current { background: var(--red); color: #fff; }

  /* Sidebar */
  .widget-icon { left: 794px; width: 37px; height: 33px; background: var(--red); display: flex; align-items: center; justify-content: center; }
  .widget-title { left: 838px; width: 157px; height: 33px; background: var(--red); color: #fff; font-family: "Libre Baskerville", Georgia, serif; font-weight: 700; font-size: 15px; line-height: 33px; padding-left: 12px;
    box-shadow: 0 8px 8px -6px rgba(0,0,0,.3); }
  .widget-list { left: 839px; list-style: none; font-size: 9.5px; color: #888; }
  .widget-list li { height: 24px; }
  .widget-list li::before { content: "›"; color: #555; margin-right: 5px; font-size: 11px; }
  .widget-list a { color: #444; text-decoration: underline; }

  /* Footer */
  .footer { left: 0; top: 928px; width: 1200px; height: 104px; background: var(--footer); }
  .footer h4 { position: absolute; font-family: "Libre Baskerville", Georgia, serif; font-weight: 700; font-size: 11px; color: var(--footer-head); }
  .footer h4 small { font-family: "Arimo", Arial, sans-serif; font-weight: 400; font-size: 9.5px; color: var(--footer-text); }
  .footer-links { position: absolute; left: 246px; top: 44px; list-style: none; font-size: 9.5px; line-height: 13.5px; }
  .footer-links a { color: var(--footer-text); text-decoration: underline; }
  .footer-divider { position: absolute; top: 36px; width: 1px; height: 58px; background: #595959; }
  .footer-about { position: absolute; left: 423px; top: 44px; width: 320px; font-size: 9.5px; line-height: 13.5px; color: var(--footer-text); }
  .footer-about em { font-style: normal; color: var(--red); }
  .copyright { position: absolute; left: 842px; top: 58px; font-family: "Libre Baskerville", Georgia, serif; font-weight: 700; font-size: 11px; color: var(--footer-head); }
</style>
</head>
<body>

<header>
  <div class="abs hero" role="img" aria-label="Panoramic close-up photograph of burgers, fries and a dish of ketchup"></div>
  <h1 class="abs site-title">TableHop London</h1>

  <form class="abs search">
    <label style="top:16px">What restaurant ?</label>
    <div class="field" style="top:40px">India
      <svg width="14" height="9" viewBox="0 0 14 9"><path d="M1 1l6 6 6-6" fill="none" stroke="#999" stroke-width="2.4"/></svg>
    </div>
    <label style="top:85px">What kind of food ?</label>
    <div class="field" style="top:108px">All</div>
    <label style="top:151px">Where ?</label>
    <div class="field" style="top:174px">Everywhere</div>
    <label style="top:213px">Prices ?*</label>
    <div class="field" style="top:241px">All</div>
    <div class="btn-search">Search</div>
  </form>

  <div class="abs tagline">
    <h2>Lorem Ipsum is simply dummy text</h2>
    <p class="sub">of the printing and typesetting industry</p>
    <p class="small">Lorem Ipsum is simply dummy text</p>
  </div>
</header>

<main>
  <h2 class="abs results-title">BEST RESTAURANTS IN <span>LONDON</span></h2>
  <div class="abs results-rule"></div>

  <div class="abs thumb" style="left:245px;top:529px"><div role="img" aria-label="Photo of colourful fresh fruit and vegetables"></div></div>
  <h3 class="abs item-name" style="left:422px;top:530px">Example 1</h3>
  <p class="abs item-desc" style="left:423px;top:568px">Lorem Ipsum is simply dummy text of the printing and typesetting industry. Lorem Ipsum has been the industry's standard dummy text ever since the 1500s, when an unknown rinter took a galley of type and scrambled it to make a type specimen book.</p>
  <span class="abs item-more" style="left:423px;top:640px">+ view</span>
  <div class="abs item-bar" style="top:662px">
    <div class="cell"><svg width="20" height="20" viewBox="0 0 20 20"><circle cx="15" cy="4" r="2.6" fill="#666"/><circle cx="4" cy="10" r="2.6" fill="#666"/><circle cx="15" cy="16" r="2.6" fill="#666"/><path d="M15 4L4 10l11 6" fill="none" stroke="#666" stroke-width="1.6"/></svg></div>
    <div class="cell"><svg width="20" height="20" viewBox="0 0 20 20"><circle cx="10" cy="10" r="8.5" fill="none" stroke="#666" stroke-width="1.8"/><path d="M10 15c-3-3.5-4-5-4-6.5a4 4 0 018 0c0 1.5-1 3-4 6.5z" fill="#666"/><circle cx="10" cy="8.5" r="1.5" fill="#fff"/></svg></div>
    <div class="cell"><svg width="16" height="20" viewBox="0 0 16 20"><rect x="1" y="1" width="5" height="4" fill="#666"/><rect x="8" y="8" width="6" height="4" fill="#666"/><rect x="8" y="15" width="6" height="4" fill="#666"/><path d="M3.5 5v12H8M3.5 10H8" fill="none" stroke="#666" stroke-width="1.4"/></svg></div>
    <div class="cell"><svg width="16" height="20" viewBox="0 0 16 20"><path d="M13 5a4 4 0 00-7 2v11M3 11h7M2 18h12" fill="none" stroke="#666" stroke-width="2.4"/></svg></div>
    <div class="rating" aria-label="Rating 2"><i></i><i></i></div>
  </div>

  <div class="abs thumb" style="left:245px;top:712px"><div role="img" aria-label="Photo of colourful fresh fruit and vegetables"></div></div>
  <h3 class="abs item-name" style="left:422px;top:713px">Example 2</h3>
  <p class="abs item-desc" style="left:423px;top:751px">Lorem Ipsum is simply dummy text of the printing and typesetting industry. Lorem Ipsum has been the industry's standard dummy text ever since the 1500s, when an unknown rinter took a galley of type and scrambled it to make a type specimen book.</p>
  <span class="abs item-more" style="left:423px;top:823px">+ view</span>
  <div class="abs item-bar" style="top:845px">
    <div class="cell"><svg width="20" height="20" viewBox="0 0 20 20"><circle cx="15" cy="4" r="2.6" fill="#666"/><circle cx="4" cy="10" r="2.6" fill="#666"/><circle cx="15" cy="16" r="2.6" fill="#666"/><path d="M15 4L4 10l11 6" fill="none" stroke="#666" stroke-width="1.6"/></svg></div>
    <div class="cell"><svg width="20" height="20" viewBox="0 0 20 20"><circle cx="10" cy="10" r="8.5" fill="none" stroke="#666" stroke-width="1.8"/><path d="M10 15c-3-3.5-4-5-4-6.5a4 4 0 018 0c0 1.5-1 3-4 6.5z" fill="#666"/><circle cx="10" cy="8.5" r="1.5" fill="#fff"/></svg></div>
    <div class="cell"><svg width="16" height="20" viewBox="0 0 16 20"><rect x="1" y="1" width="5" height="4" fill="#666"/><rect x="8" y="8" width="6" height="4" fill="#666"/><rect x="8" y="15" width="6" height="4" fill="#666"/><path d="M3.5 5v12H8M3.5 10H8" fill="none" stroke="#666" stroke-width="1.4"/></svg></div>
    <div class="cell"><svg width="16" height="20" viewBox="0 0 16 20"><path d="M13 5a4 4 0 00-7 2v11M3 11h7M2 18h12" fill="none" stroke="#666" stroke-width="2.4"/></svg></div>
    <div class="rating" aria-label="Rating 3"><i></i><i></i><i></i></div>
  </div>

  <nav class="abs pager">
    <span>&lt;&lt;</span><span class="current">1</span><span>2</span><span>3</span><span>&gt;&gt;</span>
  </nav>
</main>

<aside>
  <div class="abs widget-icon" style="top:428px"><svg width="22" height="22" viewBox="0 0 22 22"><path d="M3 5l14 14M8 2l-5 5 3 3 5-5M14 3l5 16" fill="none" stroke="#fff" stroke-width="2"/></svg></div>
  <h3 class="abs widget-title" style="top:428px">Categories</h3>
  <ul class="abs widget-list" style="top:475px">
    <li><a>Italian restaurants</a> (2)</li>
    <li><a>Italian restaurants</a> (2)</li>
  </ul>

  <div class="abs widget-icon" style="top:582px"><svg width="24" height="24" viewBox="0 0 20 20"><circle cx="10" cy="10" r="8.5" fill="none" stroke="#fff" stroke-width="1.8"/><path d="M10 15c-3-3.5-4-5-4-6.5a4 4 0 018 0c0 1.5-1 3-4 6.5z" fill="#fff"/><circle cx="10" cy="8.5" r="1.5" fill="var(--red)"/></svg></div>
  <h3 class="abs widget-title" style="top:582px">Location</h3>
  <ul class="abs widget-list" style="top:630px">
    <li><a>Restaurent in west london</a> (2)</li>
  </ul>

  <div class="abs widget-icon" style="top:702px"><svg width="18" height="24" viewBox="0 0 16 20"><path d="M13 5a4 4 0 00-7 2v11M3 11h7M2 18h12" fill="none" stroke="#fff" stroke-width="2.6"/></svg></div>
  <h3 class="abs widget-title" style="top:702px">Prices</h3>
  <ul class="abs widget-list" style="top:752px">
    <li><a>Casual restaurants(10-20)</a> (2)</li>
  </ul>
</aside>

<footer class="abs footer">
  <h4 style="left:246px;top:24px">Basic Links</h4>
  <ul class="footer-links">
    <li><a>Lorem Ipsum is simply</a></li>
    <li><a>Lorem Ipsum is simply</a></li>
    <li><a>Lorem Ipsum is simply</a></li>
    <li><a>Lorem Ipsum is simply</a></li>
  </ul>
  <div class="footer-divider" style="left:411px"></div>
  <h4 style="left:423px;top:24px">Basic Links <small>Lorem Ipsum is simply</small></h4>
  <p class="footer-about">Lorem Ipsum is simply dummy text of the printing and typesetting industry. Lorem Ipsum has <em>been the industry's standard dummy</em> text ever since the 1500s,</p>
  <div class="footer-divider" style="left:777px"></div>
  <p class="copyright">TableHop London &copy; 2013</p>
</footer>

</body>
</html>
```